Flyer Design Project

Lanterns of Yore is a new collaborative of non-profit historical sites in the Greater Boston area. We're promoting the soft launch of our website by hosting open houses at each of the sites on September 21. We need a flyer to post up at each of the sites.

I have more print design needs to follow, and would really like to have a consistent look, so I intend to directly invite the winning designer to more projects.

Industry/Entity Type

Non-Profit

Requirements
Must have
• The flyer must be one page and be delivered as two files in Microsoft Publisher OR Microsoft Word. One file is for an 8 1/2 x 11 and one is as an 11 x 17 (same design, just scaled larger to fit the bigger paper).

It must have the Lanterns of Yore Logo (attached), and this text (attached) and use black font.

Any color that is not black or white must be chosen from these colors-but don't feel you have to use all of them:

Lanterns of Yore Website Colors

poppy red
c 0
m 93
y 87
k 0
web FF3333

nectarine
c 0
m 54
y 74
k 0
web FF9966

monaco blue

c 100
m 79
y 28
k 12
web 003366

tender shoots
c 30
m 0
y 89
k 0
web CCCC33

emerald
c 80
m 11
y 56
k 0
web 009999

african violet
c 28
m 44
y 0
k 0

web CC99CC

sunflower
c 10
m 33
y 99
k 0
web FF9933

lemon zest
c 4
m 13
y 77
k 0
web FFCC66

Nice to have
• Text and images with in the flyer should be large, simple and clear-as easy to see and read when the entire flyer is viewed on a mobile phone or from a distance as possible.

```html
<!DOCTYPE html>
<html lang="en">
<head>
<meta charset="utf-8">
<title>Lanterns of Yore – Boston Open House Flyer</title>
<link href="https://fonts.googleapis.com/css2?family=Source+Sans+3:wght@400;600;700&family=Playball&display=swap" rel="stylesheet">
<style>
  :root {
    --page: #ffffff;
    --navy: #003366;
    --blue-deep: #1d4f8f;
    --blue-mid: #2f6fb3;
    --blue-tile-a: #1b6fb8;
    --blue-tile-b: #0d4f96;
    --sunflower: #FF9933;
    --ink: #1a1a1a;
    --panel-top: #f3f4f6;
    --panel-bottom: #c9ced6;
    --panel-edge: #9aa4b2;
    --mist: #e8edf2;
  }
  * { box-sizing: border-box; margin: 0; padding: 0; }
  html, body { width: 920px; height: 1200px; overflow: hidden; background: var(--page); }
  body { position: relative; font-family: "Source Sans 3", Arial, sans-serif; color: var(--ink); }

  .flyer { position: absolute; left: 48px; top: 50px; width: 839px; height: 1105px; overflow: hidden;
    background: linear-gradient(160deg, var(--blue-mid) 0%, var(--blue-deep) 60%, #174580 100%); }

  .abs { position: absolute; }

  .skyline-photo { left: 0; top: 0; width: 839px; height: 229px;
    background: linear-gradient(180deg, #3f8fd8 0%, #7fb4e4 30%, #8a9a7a 55%, #c07a3a 62%, #2c6fb0 72%, #1f5fa6 100%); }
  .city-title { position: absolute; right: 44px; top: 112px; font-family: "Playball", cursive;
    font-size: 92px; font-weight: 400; line-height: 1; color: #eef3fa; text-shadow: 2px 3px 4px rgba(0,0,40,.45); }

  .map-area { left: 498px; top: 229px; width: 341px; height: 876px;
    background: linear-gradient(180deg, #f6f7f9 0%, var(--mist) 60%, #dfe6ee 100%); }
  .grid-backing { left: 166px; top: 229px; width: 673px; height: 418px; background: var(--page); }

  .tile { position: absolute; }
  .tile.blue { background: linear-gradient(135deg, var(--blue-tile-a), var(--blue-tile-b)); }

  .info-box { left: 26px; top: 462px; width: 290px; height: 284px; border-radius: 10px;
    background: linear-gradient(180deg, var(--panel-top), var(--panel-bottom));
    border: 1px solid var(--panel-edge); padding: 10px 8px 0 12px; overflow: hidden; }
  .info-box h2 { font-size: 23px; font-weight: 700; color: var(--sunflower); line-height: 1.15; margin-bottom: 4px; }
  .info-box p { font-size: 14px; line-height: 17.6px; white-space: nowrap; }

  .callout-box { left: 18px; top: 768px; width: 463px; height: 293px; border-radius: 12px;
    background: linear-gradient(180deg, var(--panel-top), var(--panel-bottom));
    border: 1px solid var(--panel-edge); padding: 6px 8px 0 16px; overflow: hidden; }
  .callout-box h2 { font-size: 27px; font-weight: 700; color: var(--sunflower); line-height: 1.2; margin-bottom: 4px; }
  .callout-list { list-style: none; }
  .callout-list li { position: relative; padding-left: 22px; font-size: 14px; line-height: 17.8px; white-space: nowrap; }
  .callout-list li svg { position: absolute; left: 0; top: 4px; }

  .brand { left: 504px; top: 960px; width: 320px; height: 110px; display: flex; align-items: center; gap: 14px; }
  .brand-mark { width: 62px; height: 62px; background: var(--sunflower); flex: none; }
  .brand-name { font-size: 44px; font-weight: 600; line-height: 1.0; color: var(--navy); }
</style>
</head>
<body>
<main class="flyer">
  <div class="abs skyline-photo" role="img" aria-label="Photograph of the Boston skyline across the river with sailboats and autumn trees"></div>
  <h1 class="city-title">Boston</h1>

  <div class="abs map-area" role="img" aria-label="Faded street map of Boston"></div>
  <div class="abs grid-backing"></div>

  <div class="tile" style="left:2px;top:234px;width:164px;height:108px;background:linear-gradient(180deg,#1a2340,#6a4a2a 60%,#c98a3a);" role="img" aria-label="Historic brick mansion lit at dusk"></div>
  <div class="tile blue" style="left:171px;top:234px;width:149px;height:108px;"></div>
  <div class="tile" style="left:326px;top:234px;width:166px;height:108px;background:linear-gradient(180deg,#6f96c8,#d6dde6 55%,#5d8a3c);" role="img" aria-label="Granite monument on a grassy lawn"></div>
  <div class="tile blue" style="left:498px;top:234px;width:146px;height:108px;"></div>
  <div class="tile" style="left:649px;top:234px;width:174px;height:108px;background:linear-gradient(180deg,#8fb0d0,#d9c49a 50%,#4d6e2f);" role="img" aria-label="Colonial meeting house with a white steeple among trees"></div>

  <div class="tile" style="left:171px;top:348px;width:149px;height:88px;background:linear-gradient(180deg,#5f8a45,#9ab870 50%,#3c5a2c);" role="img" aria-label="Leafy cemetery with a stone obelisk and iron fence"></div>
  <div class="tile blue" style="left:326px;top:348px;width:166px;height:88px;"></div>
  <div class="tile" style="left:498px;top:348px;width:146px;height:88px;background:linear-gradient(180deg,#9cc0e0,#e69ab8 40%,#c9a060 70%,#6b8f3c);" role="img" aria-label="Pink flowering tree in front of a yellow wooden meeting house"></div>
  <div class="tile blue" style="left:649px;top:348px;width:174px;height:88px;"></div>

  <div class="tile" style="left:326px;top:441px;width:166px;height:97px;background:linear-gradient(135deg,#4a9ab8,#c8b46a 50%,#7a3a3a);" role="img" aria-label="Stained glass window with a star pattern"></div>
  <div class="tile blue" style="left:498px;top:441px;width:146px;height:97px;"></div>
  <div class="tile" style="left:649px;top:441px;width:174px;height:97px;background:linear-gradient(180deg,#6e7a80,#8a6a58 50%,#5c8a3c);" role="img" aria-label="Stone chapel entrance with a red door and garden steps"></div>

  <div class="tile" style="left:498px;top:544px;width:146px;height:97px;background:linear-gradient(180deg,#3a5a9a,#e8dcc0 55%,#8a5a30);" role="img" aria-label="Round historic building lit at dusk"></div>
  <div class="tile blue" style="left:649px;top:544px;width:174px;height:97px;"></div>

  <div class="tile" style="left:649px;top:647px;width:174px;height:101px;background:linear-gradient(180deg,#1a2a55,#3a4f9a 55%,#c98a3a);" role="img" aria-label="Cable-stayed bridge lit blue at night"></div>

  <section class="abs info-box">
    <h2>Saturday, September 21</h2>
    <p>Explorers. Pilgrims. Revolution. Civil War.<br>Industrialization. You know the history.<br>But do you know the stories? Have you<br>found how YOU are connected to the<br>places and lives of the people who’ve<br>shaped our world, our country, our state,<br>and your life today? Find out by exploring<br>some of Massachusetts’ treasured historical<br>gems—you’ll be surprised by the<br>wealth you discover.<br>For hours, directions, and<br>discount/prize passes learn more at<br>www.lanternsofyore.org</p>
  </section>

  <section class="abs callout-box">
    <h2>Call Out Box:</h2>
    <ul class="callout-list">
      <li><svg width="16" height="10" viewBox="0 0 16 10"><path d="M0 0 L16 5 L0 10 L4 5 Z" fill="#2f6fb3"/></svg>Special Tours, Games, Prizes, and Children’s Activities!</li>
      <li><svg width="16" height="10" viewBox="0 0 16 10"><path d="M0 0 L16 5 L0 10 L4 5 Z" fill="#2f6fb3"/></svg>Participating Organizations (must appear exactly as printed</li>
      <li><svg width="16" height="10" viewBox="0 0 16 10"><path d="M0 0 L16 5 L0 10 L4 5 Z" fill="#2f6fb3"/></svg>in the order listed)</li>
      <li><svg width="16" height="10" viewBox="0 0 16 10"><path d="M0 0 L16 5 L0 10 L4 5 Z" fill="#2f6fb3"/></svg>Lantern Hill at Birchwood Estate</li>
      <li><svg width="16" height="10" viewBox="0 0 16 10"><path d="M0 0 L16 5 L0 10 L4 5 Z" fill="#2f6fb3"/></svg>“Church of the Founders” Union First Parish (Unitarian) of Avon</li>
      <li><svg width="16" height="10" viewBox="0 0 16 10"><path d="M0 0 L16 5 L0 10 L4 5 Z" fill="#2f6fb3"/></svg>Ashford Memorial Library</li>
      <li><svg width="16" height="10" viewBox="0 0 16 10"><path d="M0 0 L16 5 L0 10 L4 5 Z" fill="#2f6fb3"/></svg>Marlow Dance Theatre’s Home at Old Riverside Baptist Church</li>
      <li><svg width="16" height="10" viewBox="0 0 16 10"><path d="M0 0 L16 5 L0 10 L4 5 Z" fill="#2f6fb3"/></svg>Whitcomb’s Boat Shop and Museum</li>
      <li><svg width="16" height="10" viewBox="0 0 16 10"><path d="M0 0 L16 5 L0 10 L4 5 Z" fill="#2f6fb3"/></svg>Mount Linden Cemetery</li>
      <li><svg width="16" height="10" viewBox="0 0 16 10"><path d="M0 0 L16 5 L0 10 L4 5 Z" fill="#2f6fb3"/></svg>Heritage Museum of Black History: Harbor Campus</li>
      <li><svg width="16" height="10" viewBox="0 0 16 10"><path d="M0 0 L16 5 L0 10 L4 5 Z" fill="#2f6fb3"/></svg>Heritage Museum of Black History: Island Campus</li>
      <li><svg width="16" height="10" viewBox="0 0 16 10"><path d="M0 0 L16 5 L0 10 L4 5 Z" fill="#2f6fb3"/></svg>Monument to the First Settlers</li>
      <li><svg width="16" height="10" viewBox="0 0 16 10"><path d="M0 0 L16 5 L0 10 L4 5 Z" fill="#2f6fb3"/></svg>Old Anchor Meeting House</li>
    </ul>
  </section>

  <div class="abs brand">
    <span class="brand-mark"></span>
    <span class="brand-name">Lanterns<br>of Yore</span>
  </div>
</main>
</body>
</html>
```